Mortgage company revamping our superhero brand design

We are a mortgage company called LOAN LIFTS LIVES we have superheroes as our avatars and I want to create a design that brings our slogan to the forefront. BUILDING A LEGACY BY LEVERAGING DEBT, MAKE DEBT WORK FOR YOU. In our brand debt is the hero we teach our clients how to use a mortgage to create wealth

Target Market(s)

from 20-50

Industry/Entity Type

Mortgage Brokerage

Font styles to use
Sans Serif

Requirements
Must have
• I want to use the color BLACK, WHITE with hints of RED WHITE AND BLUE
Nice to have
• We are young and modern

```html
<!DOCTYPE html>
<html lang="en">
<head>
<meta charset="utf-8">
<title>Building a Legacy by Leveraging Debt</title>
<link rel="stylesheet" href="https://fonts.googleapis.com/css2?family=Bungee&display=swap">
<style>
  :root {
    --ink: #1a1010;
    --paper: #ffffff;
    --glow-red: rgba(226, 92, 110, 0.75);
    --glow-red-soft: rgba(240, 170, 180, 0.35);
    --glow-blue: rgba(70, 86, 150, 0.75);
    --glow-blue-soft: rgba(150, 165, 210, 0.35);
    --hero-dark: #2e2420;
    --hero-mid: #6b4e3d;
    --hero-red: #c8202e;
  }
  html, body {
    margin: 0;
    padding: 0;
    overflow: hidden;
    background: var(--paper);
  }
  .poster {
    position: relative;
    width: 1200px;
    height: 914px;
    overflow: hidden;
    background:
      radial-gradient(ellipse 440px 230px at 430px 250px, var(--glow-red) 0%, var(--glow-red-soft) 55%, transparent 100%),
      radial-gradient(ellipse 470px 230px at 470px 720px, var(--glow-blue) 0%, var(--glow-blue-soft) 55%, transparent 100%),
      var(--paper);
  }
  .hero-avatar {
    position: absolute;
    left: 740px;
    top: 10px;
    width: 450px;
    height: 800px;
    border-radius: 46% 46% 40% 40% / 30% 30% 26% 26%;
    background: linear-gradient(180deg, var(--hero-mid) 0%, var(--hero-dark) 45%, var(--hero-red) 70%, var(--hero-dark) 100%);
    opacity: 0.9;
  }
  .slogan {
    position: absolute;
    inset: 0;
    width: 1200px;
    height: 914px;
  }
  .slogan text {
    font-family: "Bungee", "Arial Black", sans-serif;
    fill: var(--ink);
  }
  .slogan .headline { font-size: 130px; }
  .slogan .tagline { font-size: 80px; }
</style>
</head>
<body>
  <main class="poster">
    <div class="hero-avatar" role="img" aria-label="Cartoon superhero mascot with a beard, cape and round shield, pointing towards the slogan"></div>
    <svg class="slogan" viewBox="0 0 1200 914" xmlns="http://www.w3.org/2000/svg" aria-label="Building a legacy by leveraging debt. Make debt work for you.">
      <text class="headline" x="81" y="162" textLength="511" lengthAdjust="spacingAndGlyphs">BUILDING</text>
      <text class="headline" x="324" y="276" textLength="62" lengthAdjust="spacingAndGlyphs">A</text>
      <text class="headline" x="73" y="409" textLength="397" lengthAdjust="spacingAndGlyphs">LEGACY</text>
      <text class="headline" x="308" y="535" textLength="122" lengthAdjust="spacingAndGlyphs">BY</text>
      <text class="headline" x="36" y="665" textLength="678" lengthAdjust="spacingAndGlyphs">LEVERAGING</text>
      <text class="headline" x="260" y="779" textLength="260" lengthAdjust="spacingAndGlyphs">DEBT</text>
      <text class="tagline" x="97" y="889" textLength="811" lengthAdjust="spacingAndGlyphs">MAKE DEBT WORK FOR YOU</text>
    </svg>
  </main>
</body>
</html>
```